New Coffee Brand Packaging Design

We need a package design for our new coffee brand called Brindle Oak Coffee. Our brand mission will be displayed on the packaging (along the side or the back) and we currently have a logo that should be displayed on the front. Feel free to suggest a new logo design as you are designing the packaging if it doesn't fit with your vision. The final design should be creative and conservative. We like coffee colors (dark and light browns, white, cream, black, gold). We also like chalkboard art imagery (i.e. coffee cups, theme words from our mission, people, etc.). One famous person from Millbrook Heights, OH is Terrence Vogt (world famous boxer and activist). If there is a way to draw his image in more of an abstract way where it doesn't infringe any patents that would be the sort of creativity we would like in the packaging. Our coffee brand prides itself on being a coffee for the people. For the average joe, working American who enjoys a good cup of coffee and a good atmosphere.

Brindle Oak Coffee Mission: "We aim to be a coffee company for the people. The people who have an appreciation and love for family, community and who never forget where they came from. Our coffee was born out of Millbrook Heights, OH…a place like many others where the hearts, the minds and the wills are strong. We hope you enjoy each and every cup. Peace & Blessings."

Requirements
Must have
• (On the side or on the back of the packaging) Brindle Oak Coffee Mission: "We aim to be a coffee company for the people. The people who have an appreciation and love for family, community and who never forget where they came from. Our coffee was born out of Millbrook Heights, OH…a place like many others where the hearts, the minds and the wills are strong. We hope you enjoy each and every cup. Peace & Blessings."
Nice to have
• Coffee Colors: dark and light browns, white, cream, black, gold

```html
<!DOCTYPE html>
<html lang="en">
<head>
<meta charset="utf-8">
<title>Brindle Oak Coffee – Bag Packaging</title>
<link rel="stylesheet" href="https://fonts.googleapis.com/css2?family=Signika:wght@400;600&display=swap">
<style>
  :root {
    --backdrop: #3f2620;
    --bag-white: #ffffff;
    --bean-dark: #3b1a12;
    --bean-mid: #6b3a24;
    --label-brown: #7b4a3c;
    --label-text: #ffffff;
    --mission-text: #4a1e14;
    --brand-ink: #1f1412;
  }
  html, body {
    margin: 0;
    padding: 0;
    width: 1200px;
    height: 856px;
    overflow: hidden;
    background: var(--backdrop);
  }
  .canvas {
    position: relative;
    width: 1200px;
    height: 856px;
    background: var(--backdrop);
    font-family: "Signika", "Trebuchet MS", sans-serif;
  }
  .bags {
    position: absolute;
    inset: 0;
  }
  .bag-body { fill: var(--bag-white); }

  .product-label {
    position: absolute;
    left: 250px;
    top: 205px;
    width: 186px;
    height: 57px;
    background: var(--label-brown);
    color: var(--label-text);
    box-sizing: border-box;
    display: flex;
    flex-direction: column;
    justify-content: center;
    align-items: center;
    font-size: 14px;
    font-weight: 400;
    line-height: 17px;
  }
  .product-label::before,
  .product-label::after {
    content: "";
    position: absolute;
    left: 6px;
    right: 6px;
    height: 1px;
    background: var(--label-text);
  }
  .product-label::before { top: 6px; }
  .product-label::after { bottom: 6px; }

  .brand-mark {
    position: absolute;
    width: 300px;
    text-align: center;
    color: var(--brand-ink);
    font-weight: 400;
    top: 672px;
  }
  .brand-mark .brand-name {
    display: block;
    font-size: 44px;
    line-height: 48px;
  }
  .brand-mark .brand-word {
    display: block;
    font-size: 19px;
    letter-spacing: 4px;
    line-height: 22px;
    padding-left: 150px;
  }
  .brand-mark--front { left: 190px; }
  .brand-mark--back { left: 740px; }

  .mission {
    position: absolute;
    left: 755px;
    top: 459px;
    width: 270px;
    text-align: center;
    color: var(--mission-text);
    font-size: 13px;
    font-weight: 400;
    line-height: 16px;
  }
  .mission p { margin: 0; }
  .mission .mission-title,
  .mission .sign-off { font-weight: 600; }
  .mission .closing { margin-top: 14px; }
</style>
</head>
<body>
<div class="canvas">
  <svg class="bags" width="1200" height="856" viewBox="0 0 1200 856">
    <defs>
      <path id="bag-outline" d="M118 120 H562 C556 170 548 200 548 235 L530 738 Q528 765 503 765 H177 Q150 765 148 738 L132 235 C132 200 124 170 118 120 Z"/>
      <clipPath id="clip-front"><use href="#bag-outline"/></clipPath>
      <clipPath id="clip-back"><use href="#bag-outline" transform="translate(550 0)"/></clipPath>
      <linearGradient id="bean-fill" x1="0" y1="0" x2="0" y2="1">
        <stop offset="0" stop-color="#3b1a12"/>
        <stop offset="0.6" stop-color="#6b3a24" stop-opacity="0.85"/>
        <stop offset="1" stop-color="#e8892a" stop-opacity="0"/>
      </linearGradient>
    </defs>

    <g class="bag bag--front">
      <use class="bag-body" href="#bag-outline"/>
      <rect class="bean-illustration" role="img" aria-label="Scattered dark brown and orange coffee beans falling from the top of the bag"
            x="110" y="115" width="460" height="330" fill="url(#bean-fill)" clip-path="url(#clip-front)"/>
    </g>

    <g class="bag bag--back">
      <use class="bag-body" href="#bag-outline" transform="translate(550 0)"/>
      <rect class="bean-illustration" role="img" aria-label="Scattered dark brown and orange coffee beans falling from the top of the bag"
            x="660" y="115" width="460" height="330" fill="url(#bean-fill)" clip-path="url(#clip-back)"/>
    </g>
  </svg>

  <div class="product-label">
    <span>Whole Bean Coffee</span>
    <span>Net Weight 16oz.</span>
  </div>

  <div class="brand-mark brand-mark--front">
    <span class="brand-name">Brindle Oak</span>
    <span class="brand-word">COFFEE</span>
  </div>

  <div class="mission">
    <p class="mission-title">Brindle Oak Coffee Mission:</p>
    <p>We aim to be a coffee company for the people.<br>
       The people who have an appreciation and love<br>
       for family, community and who never forget<br>
       where they came from. Our coffee was born<br>
       out of Millbrook Heights, OH…<br>
       A place like many others where the hearts,<br>
       the minds and the wills are strong.</p>
    <p class="closing">We hope you enjoy each and every cup.</p>
    <p class="sign-off">Peace &amp; Blessings</p>
  </div>

  <div class="brand-mark brand-mark--back">
    <span class="brand-name">Brindle Oak</span>
    <span class="brand-word">COFFEE</span>
  </div>
</div>
</body>
</html>
```